Pool & Hot Tub Company Need Vehicle Wrap Designs

We need vehicle wrap designs for a Pool & Hot Tub company based in Vancouver, Canada. We do weekly maintenance and repairs. These wraps will be for a 2022 Halvorden Kesta. We are looking for something clean and modern but not boring with a bunch of lines and text. Although we service both pools and hot tubs, this design needs to be hot tub specific. We will be needing future designs for the pool division as well as the repair division, and we would like them all to be cohesive but each have their own differences highlighting their specific divisions. This design will be specifically for the hot tub division. Colours to be used are, White, Blue, Black, Grey. The specific vehicle used is a 2022 Halvorden Kesta, please use that in the mockup. If not able to use a Kesta, please use a small SUV, but Kesta is definitely preferred.
Creative freedom is encouraged. Please include the following info as a minimum: Website, Phone, Email, Services Provided.

www.ferncrestpoolandspa.com
(604)555-0183
service@ferncrestpools.com

Services Provided:
*Weekly Maintenace.
*Repairs.
*Water Changes.

Target Market(s)

Mid to Upper Class Clientel with $200k+/year salary

Industry/Entity Type

Pool & Hot Tub Service - Weekly Water Maintenance & Repairs

Font styles to use
Sans Serif

Colors
0054AA
0677BA
7BADD7
CADEEF
E8F1F8
0094D4
00A9DD
6FCCEA
C7EBF8
E9F6FB
00AB8E
00BBA5
67D7C9
C6EFE9
E9F9F6

Requirements
Must have
• Our logo , services provided, contact info, website.
Should not have
• A bunch of text an clustered design

```html
<!DOCTYPE html>
<html lang="en">
<head>
<meta charset="utf-8">
<title>Ferncrest Pool &amp; Spa – Hot Tub Division Vehicle Wrap, Driver Side</title>
<link href="https://fonts.googleapis.com/css2?family=Montserrat:wght@600;700&family=Open+Sans:wght@600;700&display=swap" rel="stylesheet">
<style>
  :root {
    --page-bg: #eef1f4;
    --wrap-white: #ffffff;
    --wrap-blue: #1e9fe3;
    --wrap-blue-deep: #0677ba;
    --wrap-navy: #0b2a55;
    --wrap-sky: #c7ebf8;
    --wrap-mist: #e9f6fb;
    --glass: #3b4653;
    --trim: #2c2f33;
    --bullet: #00a9dd;
  }
  html, body {
    margin: 0;
    width: 1200px;
    height: 672px;
    overflow: hidden;
    background: var(--page-bg);
  }
  .wrap-canvas {
    position: relative;
    width: 1200px;
    height: 672px;
  }
  .wrap-art {
    position: absolute;
    inset: 0;
    width: 1200px;
    height: 672px;
  }
  .brand-name {
    font-family: "Montserrat", sans-serif;
    font-weight: 700;
    font-size: 31px;
    letter-spacing: 3px;
    fill: var(--wrap-navy);
  }
  .brand-tagline {
    font-family: "Montserrat", sans-serif;
    font-weight: 600;
    font-size: 15px;
    letter-spacing: 6px;
    fill: var(--wrap-navy);
  }
  .division-label {
    font-family: "Montserrat", sans-serif;
    font-weight: 700;
    font-size: 24px;
    letter-spacing: 2px;
    fill: var(--wrap-navy);
  }
  .division-sub {
    font-family: "Montserrat", sans-serif;
    font-weight: 600;
    font-size: 13px;
    letter-spacing: 4px;
    fill: var(--wrap-blue-deep);
  }
  .contact-line {
    font-family: "Open Sans", sans-serif;
    font-weight: 700;
    font-size: 12px;
    fill: var(--wrap-blue-deep);
  }
  .service-item {
    font-family: "Open Sans", sans-serif;
    font-weight: 600;
    font-size: 12px;
    fill: var(--wrap-navy);
  }
  .service-bullet { fill: var(--bullet); }
  .phone-number {
    font-family: "Open Sans", sans-serif;
    font-weight: 700;
    font-size: 29px;
    fill: var(--wrap-white);
  }
</style>
</head>
<body>
<main class="wrap-canvas">
  <svg class="wrap-art" viewBox="0 0 1200 672" xmlns="http://www.w3.org/2000/svg">
    <defs>
      <clipPath id="body-shape">
        <path d="M72 392 L98 332 Q200 285 302 272 L355 272 L528 170 Q700 160 906 158 L1027 189 L1125 423 L1125 502
                 L1034 502 A102 102 0 0 0 830 502 L347 502 A102 102 0 0 0 143 502 L72 502 Z"/>
      </clipPath>
    </defs>

    <g class="wrap-body" clip-path="url(#body-shape)">
      <rect class="base-white" x="60" y="150" width="1080" height="360" fill="var(--wrap-white)"/>

      <path class="upper-blue" fill="var(--wrap-blue)"
            d="M60 150 L790 150 Q760 250 740 330 L360 340 Q200 340 60 360 Z"/>

      <path class="swoosh" fill="var(--wrap-sky)" opacity="0.8"
            d="M140 380 Q330 350 520 395 Q420 385 300 395 Q210 405 140 420 Z"/>
      <path class="swoosh" fill="var(--wrap-sky)" opacity="0.7"
            d="M330 420 Q450 395 600 420 Q470 415 370 445 Z"/>

      <path class="rear-navy" fill="var(--wrap-navy)"
            d="M1030 265 L1140 240 L1140 510 L1030 510 Q1070 420 1030 265 Z"/>

      <path class="phone-band" fill="var(--wrap-navy)"
            d="M545 414 L835 414 L830 457 L528 457 Z"/>

      <rect class="lower-trim" x="60" y="480" width="1080" height="30" fill="var(--trim)"/>
    </g>

    <path class="side-glass" fill="var(--glass)" d="M423 219 L642 189 L642 291 L362 291 Z"/>

    <path class="arch-trim" fill="none" stroke="var(--trim)" stroke-width="10"
          d="M143 502 A102 102 0 0 1 347 502 M830 502 A102 102 0 0 1 1034 502"/>

    <!-- hot tub division label on rear quarter -->
    <text class="division-label" x="902" y="270" text-anchor="middle">HOT TUB</text>
    <text class="division-sub" x="904" y="292" text-anchor="middle">DIVISION</text>

    <!-- brand -->
    <text class="brand-name" x="372" y="386">FERNCREST</text>
    <text class="brand-tagline" x="374" y="408">POOL &amp; SPA</text>
    <text class="contact-line" x="372" y="447">FerncrestPoolAndSpa.com</text>
    <text class="contact-line" x="372" y="472">service@ferncrestpools.com</text>

    <!-- services -->
    <g class="services">
      <circle class="service-bullet" cx="647" cy="364" r="4"/>
      <text class="service-item" x="657" y="368">WEEKLY MAINTENACE</text>
      <circle class="service-bullet" cx="647" cy="381" r="4"/>
      <text class="service-item" x="657" y="385">REPAIRS</text>
      <circle class="service-bullet" cx="647" cy="396" r="4"/>
      <text class="service-item" x="657" y="400">WATER CHANGES</text>
    </g>

    <!-- phone -->
    <g class="phone-icon" transform="translate(558 425)" fill="var(--bullet)">
      <path d="M3 0 L8 0 L10 6 L7 8 Q9 14 14 17 L16 14 L22 16 L22 21 Q20 24 16 23 Q2 18 0 4 Q0 1 3 0 Z"/>
    </g>
    <text class="phone-number" x="587" y="446">(604)555-0183</text>
  </svg>
</main>
</body>
</html>
```